Adult Gif banners for lustvale required

Hi guys I'm wanting to do some targeted advertising via signal brook on lustvale but I'm struggling with the banners I'd want animated Gif one I have my own logo and videos to turn into gif ect the banners need to be 

300 × 250

305 × 99

950 × 250

300 × 150

These are the sizes they have given me but I'm not really sure what ones are what 

when I visit lustvale on my phone I see a box at the top of the page and one at the bottom ill add  screenshots so you can see 

ideally id like those sizes for mobile devices people use there mobiles more than desktop for stuff like lustvale

Their site says also says this about sizing of the files 

"Static banner ads use static .jpg/.png or animated .gif creatives that have a maximum size of 300KB."
Ive added my logo video ect and a screenshot of the size i require

"Video banner ads use video creatives that have a maximum size of 1MB. Usually, these banners play without sound."

hope this helps I'll look for to your response thank you (Delia Marwenn)

Target Market(s)

Adult audience

Industry/Entity Type

Adult entertainment

Colors
E54698
E96AAD
F1A4CE
F9D9EA
FCEFF6

Requirements
Must have
• Gif video

```html
<!DOCTYPE html>
<html lang="en">
<head>
<meta charset="utf-8">
<title>Lustvale Banner Set</title>
<link rel="stylesheet" href="https://fonts.googleapis.com/css2?family=Montserrat:wght@500;700;800&display=swap">
<style>
  :root {
    --stage: #6a6a6a;
    --size-label: #a3a3a3;
    --pink-soft: #f1a4ce;
    --pink-strong: #e54698;
    --white: #ffffff;
    --photo-dark: #0d0b06;
    --photo-mid: #2e2418;
    --photo-warm: #8a7358;
  }
  * { margin: 0; padding: 0; box-sizing: border-box; }
  html, body { width: 1200px; height: 794px; overflow: hidden; }
  body {
    background: var(--stage);
    font-family: "Montserrat", Arial, sans-serif;
    position: relative;
  }
  .banner {
    position: absolute;
    background: var(--pink-soft);
    box-shadow: 3px 4px 6px rgba(0,0,0,0.35);
    overflow: hidden;
  }
  .banner-photo {
    position: absolute;
    top: 0; bottom: 0; right: 0;
    background:
      radial-gradient(ellipse 22% 42% at 60% 48%, rgba(200,180,150,0.55) 0%, rgba(138,115,88,0.25) 55%, transparent 100%),
      radial-gradient(ellipse at 60% 55%, var(--photo-warm) 0%, var(--photo-mid) 35%, var(--photo-dark) 75%);
  }
  .logo {
    position: absolute;
    color: var(--white);
    font-weight: 800;
    line-height: 1;
    white-space: nowrap;
  }
  .message-box {
    position: absolute;
    left: 0;
    background: var(--pink-strong);
    z-index: 2;
  }
  .message-frame {
    position: absolute;
    left: 0;
    border-right: 1px solid var(--pink-strong);
    border-bottom: 1px solid var(--pink-strong);
    z-index: 1;
  }
  .headline {
    position: absolute;
    color: var(--white);
    font-weight: 800;
    white-space: nowrap;
  }
  .cta {
    position: absolute;
    background: var(--white);
    color: var(--pink-strong);
    font-weight: 500;
    display: flex;
    align-items: center;
    justify-content: center;
    white-space: nowrap;
    line-height: 1;
  }
  .size-label {
    position: absolute;
    left: 0; width: 1200px;
    text-align: center;
    color: var(--size-label);
    font-weight: 800;
    font-size: 18px;
    line-height: 1;
  }

  /* 300 x 250 */
  .banner-medium { left: 425px; top: 46px; width: 342px; height: 284px; }
  .banner-medium .banner-photo { left: 111px; }
  .banner-medium .logo { left: 10px; top: 20px; font-size: 17px; }
  .banner-medium .message-box { top: 143px; width: 196px; height: 104px; }
  .banner-medium .message-frame { top: 149px; width: 204px; height: 105px; }
  .banner-medium .headline { left: 11px; top: 6px; font-size: 28px; line-height: 28px; }
  .banner-medium .cta { left: 11px; top: 77px; width: 113px; height: 18px; border-radius: 9px; font-size: 12.5px; }

  /* 950 x 250 */
  .banner-wide { left: 59px; top: 418px; width: 1082px; height: 284px; }
  .banner-wide .banner-photo { left: 709px; }
  .banner-wide .logo { left: 33px; top: 27px; font-size: 38px; }
  .banner-wide .message-box { top: 94px; width: 732px; height: 140px; }
  .banner-wide .message-frame { top: 104px; width: 741px; height: 141px; }
  .banner-wide .headline { left: 32px; top: 16px; font-size: 55px; line-height: 1.1; }
  .banner-wide .cta { left: 33px; top: 94px; width: 164px; height: 26px; border-radius: 8px; font-size: 18px; }
</style>
</head>
<body>
  <section class="banner banner-medium" aria-label="300 by 250 banner">
    <div class="banner-photo" role="img" aria-label="Moody studio photo of a model against a dark background"></div>
    <div class="logo">LUSTVALE</div>
    <div class="message-frame"></div>
    <div class="message-box">
      <p class="headline">YOUR TEXT<br>GOES HERE</p>
      <a class="cta">CLICK HERE</a>
    </div>
  </section>
  <p class="size-label" style="top:352px;">300 X 250</p>

  <section class="banner banner-wide" aria-label="950 by 250 banner">
    <div class="banner-photo" role="img" aria-label="Moody studio photo of a model against a dark background"></div>
    <div class="logo">LUSTVALE</div>
    <div class="message-frame"></div>
    <div class="message-box">
      <p class="headline">YOUR TEXT GOES HERE</p>
      <a class="cta">CLICK HERE</a>
    </div>
  </section>
  <p class="size-label" style="top:734px;">950 X 250</p>
</body>
</html>
```